Design a Professional Business Card for Velmora Arcs

Design a business card for Velmora Arcs, we are a National Sport Court Company.

West Region Address: 4175 Quill Harbor Ln, Suite #215 Ashcombe, Colorado 80467
East Region Address: 3817 Tamsin Rd E, Marlow Bay, Florida 34583

Target Market(s)

High End Residential & Institutional Clients

Industry/Entity Type

Design & Construction

Contact Information for Business Card

Logo/Brand/Colors/ name, number (provided in comments)

Requirements
Must have
• Colors only provided in logo
Should not have
• Any other colors not in existing logo (attached)

```html
<!DOCTYPE html>
<html lang="en">
<head>
<meta charset="utf-8">
<title>Velmora Arcs – Business Card</title>
<link href="https://fonts.googleapis.com/css2?family=Poppins:wght@400;500;600&display=swap" rel="stylesheet">
<style>
  :root {
    --navy: #1c3564;
    --green: #126434;
    --white: #ffffff;
    --page: #f4f5f7;
    --faint: #c9cbd9;
  }
  html, body {
    margin: 0; padding: 0;
    width: 1200px; height: 1200px;
    overflow: hidden;
    background: var(--page);
    font-family: "Poppins", sans-serif;
  }
  .card {
    position: absolute;
    left: 310px;
    width: 579px; height: 331px;
    background: var(--white);
    overflow: hidden;
    box-shadow: 0 0 0 1px #e2e4ea;
  }
  .card--front { top: 237px; }
  .card--back { top: 632px; }
  .card svg.shapes { position: absolute; left: 0; top: 0; }

  .person { position: absolute; left: 27px; top: 32px; color: var(--white); }
  .person__name { font-size: 21px; font-weight: 600; line-height: 1.1; margin: 0; }
  .person__role { font-size: 15px; font-weight: 400; margin: 2px 0 0; }

  .contacts { position: absolute; left: 37px; top: 107px; margin: 0; padding: 0; list-style: none; }
  .contacts li {
    display: flex; align-items: center; gap: 10px;
    height: 22.7px; font-size: 15.5px; color: var(--navy);
  }
  .contacts svg { width: 14px; height: 14px; flex: none; }

  .brand { position: absolute; display: flex; align-items: center; }
  .brand__dot { border-radius: 50%; background: var(--navy); flex: none; }
  .brand__name { color: var(--navy); font-weight: 600; text-transform: uppercase; line-height: 0.95; }

  .brand--small { left: 39px; top: 246px; gap: 12px; }
  .brand--small .brand__dot { width: 56px; height: 56px; }
  .brand--small .brand__name { font-size: 23px; letter-spacing: 1px; }

  .brand--large { left: 140px; top: 55px; gap: 22px; }
  .brand--large .brand__dot { width: 80px; height: 80px; }
  .brand--large .brand__name { font-size: 36px; letter-spacing: 1.5px; }

  .emblem { position: absolute; left: 363px; top: 121px; width: 192px; height: 192px; border-radius: 50%; background: var(--faint); }

  .addresses {
    position: absolute; left: 44px; top: 208px; width: 491px;
    text-align: center; color: var(--white); font-size: 14.8px; line-height: 17.5px;
  }
  .addresses p { margin: 0 0 18px; }
</style>
</head>
<body>

<section class="card card--front">
  <svg class="shapes" width="579" height="331" viewBox="0 0 579 331" aria-hidden="true">
    <polygon points="0,0 352,0 300,86 0,86" fill="var(--green)"/>
    <polygon points="352,26 579,26 579,35 416,35 385,86 313,86" fill="var(--navy)"/>
  </svg>
  <div class="person">
    <p class="person__name">Daniel R. Hollis, VCD</p>
    <p class="person__role">CEO &amp; Founder</p>
  </div>
  <ul class="contacts">
    <li><svg viewBox="0 0 24 24"><path fill="var(--green)" d="M6.6 10.8a15.1 15.1 0 0 0 6.6 6.6l2.2-2.2c.3-.3.7-.4 1-.2 1.1.4 2.3.6 3.6.6.6 0 1 .4 1 1V20c0 .6-.4 1-1 1A17 17 0 0 1 3 4c0-.6.4-1 1-1h3.5c.6 0 1 .4 1 1 0 1.3.2 2.5.6 3.6.1.3 0 .7-.2 1z"/></svg>(303) 555-0147</li>
    <li><svg viewBox="0 0 24 24"><path fill="var(--green)" d="M6.6 10.8a15.1 15.1 0 0 0 6.6 6.6l2.2-2.2c.3-.3.7-.4 1-.2 1.1.4 2.3.6 3.6.6.6 0 1 .4 1 1V20c0 .6-.4 1-1 1A17 17 0 0 1 3 4c0-.6.4-1 1-1h3.5c.6 0 1 .4 1 1 0 1.3.2 2.5.6 3.6.1.3 0 .7-.2 1z"/></svg>1-800-555-0192</li>
    <li><svg viewBox="0 0 24 24"><rect x="2" y="5" width="20" height="14" fill="var(--green)"/><path d="M2 5l10 8 10-8" fill="none" stroke="var(--white)" stroke-width="1.6"/></svg>daniel@velmoraarcs.com</li>
    <li><svg viewBox="0 0 24 24"><circle cx="12" cy="12" r="10" fill="var(--green)"/><path d="M2 12h20M12 2v20M5 6.5h14M5 17.5h14" stroke="var(--white)" stroke-width="1.3" fill="none"/><ellipse cx="12" cy="12" rx="4.5" ry="10" fill="none" stroke="var(--white)" stroke-width="1.3"/></svg>www.velmoraarcs.com</li>
  </ul>
  <div class="brand brand--small">
    <span class="brand__dot"></span>
    <span class="brand__name">Velmora<br>Arcs</span>
  </div>
  <div class="emblem" role="img" aria-label="Faint brand emblem decoration"></div>
</section>

<section class="card card--back">
  <svg class="shapes" width="579" height="331" viewBox="0 0 579 331" aria-hidden="true">
    <rect x="0" y="246" width="579" height="85" fill="var(--green)"/>
    <polygon points="86,199 535,199 482,309 44,309" fill="var(--navy)"/>
  </svg>
  <div class="brand brand--large">
    <span class="brand__dot"></span>
    <span class="brand__name">Velmora<br>Arcs</span>
  </div>
  <div class="addresses">
    <p>West Region Address: 4175 Quill Harbor Ln<br>Suite #215 Ashcombe, Colorado 80467</p>
    <p>East Region Address: 3817 Tamsin Rd E<br>Marlow Bay, Florida 34583</p>
  </div>
</section>

</body>
</html>
```